Consulting Group Website Landing Page Design

We are working with a Consulting Group in California. They provide consulting services to law enforcement agencies throughout the US.
Some sites to use for content:
https://www.marlowcrestcenter.org
https://www.jpellingroup.com
https://www.48rkventures.com
https://www.vdq.org
http://www.themirvalgroup.com
Thank you for taking the time to consider designing a website for us. We are web developers based in Stockton, CA, USA. Most of our projects go through the same process. Understanding this process may help you win a project with us. We custom-code all of our websites in-house. We don’t have any requirements as to what tools you use for your design, but we ask that you follow these guidelines. Plus, please send your designs in at least 1200px. wide so they do not pixelate when we show the client.
IMAGES:
If you use any images or icons in the design, we ask that you have a link to the asset so we can purchase the image/icon. Most of the designs we submit do not have the customer’s images on them unless they have some great images. Be creative; show us the feeling you are trying to portray with your image choices. Use any royalty-free site you choose. We subscribe to Velmora and mainly use their images, but we can purchase images outside of Velmora. PLEASE NOTE: we will not submit designs to clients with watermarks on the images.
FONTS:
We ask that you identify the fonts you’re using in the design. This can be done in a message if you want. We typically use Quintet Fonts and Velmora Fonts.
CONTENT:
We're always open to different content and ideas. We often submit designs with stock images so the client can see our vision. We typically take pictures after the website launch to use their images with our vision. Lorem Ipsum is fine for paragraphs, but we ask that you make the Headers with correct English. We want to be able to show the vision and identify the sections of the website.
INSPIRATION:
We typically add a couple of links in the brief of websites we like to help you get started in your design.
REVISIONS:
We do not often ask for revisions of the designs unless we see something in the design that may not appeal to the client. If there are slight changes that we want to make, we do that in the development process.
FEEDBACK:
We rarely give feedback on designs during the design process. We are working on many website projects and do not have the time to provide feedback. We usually respond if your request is well thought out and asks specific questions, but a note asking “feedback, please” usually goes unanswered.

```html
<!DOCTYPE html>
<html lang="en">
<head>
<meta charset="utf-8">
<title>Tidemark Consulting</title>
<link href="https://fonts.googleapis.com/css2?family=Questrial&family=Roboto:wght@400;500;700&display=swap" rel="stylesheet">
<style>
:root{
  --green:#74b81f;
  --green-dark:#5f9a16;
  --blue:#0a3d85;
  --blue-deep:#083270;
  --ink:#1d1d1d;
  --muted:#666;
  --grey:#f2f2f2;
  --white:#fff;
}
*{box-sizing:border-box;margin:0;padding:0}
html,body{width:1200px;height:4295px;overflow:hidden;background:var(--white)}
body{font-family:"Roboto",sans-serif;color:var(--ink)}
.page{position:relative;width:1200px;height:4295px;overflow:hidden}
.abs{position:absolute}
.heading{font-family:"Questrial",sans-serif;font-weight:400;color:var(--ink);font-size:35px;letter-spacing:-.5px}
.rule{display:inline-block;width:82px;height:2px;background:var(--green);vertical-align:middle;margin:0 14px}
.btn{position:absolute;display:flex;align-items:center;justify-content:center;background:var(--green);color:var(--white);font:500 13px "Roboto",sans-serif;text-transform:uppercase;gap:5px}
.btn .dot{width:10px;height:10px;border-radius:50%;background:var(--white);position:relative}
.btn .dot::after{content:"";position:absolute;left:3px;top:3px;border-left:4px solid var(--green);border-top:2px solid transparent;border-bottom:2px solid transparent}

/* header */
.header{top:0;left:0;width:1200px;height:77px;background:var(--white)}
.brand{left:110px;top:20px;display:flex;align-items:center;gap:8px;font:400 30px "Questrial",sans-serif;color:var(--blue)}
.brand .mark{width:32px;height:32px;border-radius:50%;background:var(--green)}
.nav{top:28px;font:500 14px "Roboto",sans-serif;color:var(--ink)}
.nav.active{color:var(--green);border-bottom:2px solid var(--green);padding-bottom:4px}
.call{left:877px;top:17px;width:210px;height:40px;border-radius:20px;font-size:13px;text-transform:none}

/* hero */
.hero{top:77px;left:0;width:1200px;height:640px;background:linear-gradient(180deg,#9ec3ea 0%,#c9d9e8 35%,#8d8f93 70%,#5d6a58 100%)}
.hero-disc{left:134px;top:94px;width:466px;height:466px;border-radius:50%;background:rgba(10,61,133,.72)}
.hero-title{left:168px;top:218px;font:400 72px/1.02 "Questrial",sans-serif;color:var(--white);letter-spacing:-1px}
.hero .btn{left:172px;top:370px;width:150px;height:40px;border-radius:20px}
.hero-curve{left:0;top:560px}
.down{left:580px;top:700px;width:40px;height:40px;border-radius:50%;background:var(--white);box-shadow:0 1px 6px rgba(0,0,0,.2)}

/* about */
.about-text{left:112px;top:867px;width:446px;font-size:13.5px;line-height:26px;color:var(--muted);text-align:justify}
.about-text p+p{margin-top:24px}
.about-mark{left:660px;top:820px;width:370px;height:370px;border-radius:50%;border:34px solid var(--blue);display:flex;align-items:center;justify-content:center;font:400 44px "Questrial",sans-serif;color:var(--green)}

/* services */
.services-bg{left:600px;top:1295px;width:600px;height:605px;background:var(--grey)}
.card{top:1460px;width:311px;height:340px;background:var(--white);box-shadow:0 2px 10px rgba(0,0,0,.08);text-align:center;padding:30px 36px 0}
.card .icon{width:70px;height:70px;margin:0 auto 14px;border:3px solid var(--green);border-radius:50%}
.card h3{font:500 19px/26px "Roboto",sans-serif;color:var(--ink);min-height:52px;display:flex;align-items:center;justify-content:center}
.card p{font-size:13.5px;line-height:21px;color:var(--muted);margin-top:8px}
.card .more{margin-top:16px;font:500 13px "Roboto",sans-serif;color:var(--green)}
.card.featured{background:var(--green)}
.card.featured .icon{border-color:var(--white)}
.card.featured h3,.card.featured p,.card.featured .more{color:var(--white)}
.card.featured .more{text-decoration:underline}
.chev{width:20px;height:34px}

/* advisers */
.advisers{top:1902px;left:0;width:1200px;height:748px;background:var(--blue)}
.advisers .heading{color:var(--white)}
.tile{display:flex;flex-direction:column;align-items:center;justify-content:center;gap:20px;font:500 16px "Roboto",sans-serif}
.tile .glyph{width:62px;height:62px;border-radius:12px;border:3px solid currentColor}
.tile.green{background:var(--green);color:var(--white)}
.tile.white{background:var(--white);color:var(--ink)}
.tile.white .glyph{border-color:var(--green)}
.photo{background:linear-gradient(135deg,#d9dfe4,#9aa6b0 55%,#4c5663)}

/* blog */
.post{top:2833px;width:310px;height:414px;border:1px solid #ddd;background:var(--white)}
.post .thumb{height:217px;background:linear-gradient(135deg,#cfd6dc,#7f8890 60%,#3d444c)}
.post h4{font:500 19px/26px "Roboto",sans-serif;margin:20px 24px 0}
.post p{font-size:13.5px;line-height:25px;color:var(--muted);margin:12px 24px 0}
.post .meta{display:flex;justify-content:space-between;align-items:center;margin:14px 24px 0}
.post .go{width:30px;height:30px;border-radius:50%;background:var(--green);position:relative}
.post .go::after{content:"";position:absolute;left:12px;top:11px;border-left:6px solid var(--white);border-top:4px solid transparent;border-bottom:4px solid transparent}
.post .date{font-size:13.5px;color:var(--green);text-decoration:underline}

/* contact */
.touch{top:3358px;left:0;width:1200px;height:650px;background:linear-gradient(160deg,#7cc126,#6aad18 60%,#77b921)}
.touch .heading{color:var(--white)}
.field{background:var(--white);border:1px solid #ccc;font-size:12px;color:#555;padding:12px 18px}
.submit{left:522px;top:3813px;width:156px;height:45px;background:var(--blue);color:var(--white);font:700 12px "Roboto",sans-serif;display:flex;align-items:center;justify-content:center}

/* footer */
.footer-curve{left:0;top:3940px}
.footer{top:4010px;left:0;width:1200px;height:285px;background:var(--blue);color:var(--white);font-size:13.5px}
.frow{position:absolute;left:0;width:1200px;display:flex;justify-content:center;gap:16px}
.ico{display:inline-block;width:10px;height:10px;background:var(--green);border-radius:50% 50% 50% 0;margin-right:6px;vertical-align:middle}
.social{top:4208px;width:30px;height:30px;border-radius:50%;background:var(--green)}
.totop{left:1048px;top:4205px;width:40px;height:40px;border-radius:50%;background:var(--white)}
</style>
</head>
<body>
<div class="page">

  <!-- header -->
  <header class="abs header">
    <div class="abs brand"><span class="mark"></span>Tidemark Consulting</div>
    <span class="abs nav active" style="left:475px">Home</span>
    <span class="abs nav" style="left:538px">About</span>
    <span class="abs nav" style="left:602px">Services</span>
    <span class="abs nav" style="left:685px">Blog</span>
    <span class="abs nav" style="left:738px">Contact</span>
    <div class="btn call">
      <svg width="12" height="12" viewBox="0 0 24 24"><path fill="#fff" d="M6.6 10.8a15 15 0 0 0 6.6 6.6l2.2-2.2c.3-.3.7-.4 1-.2 1.1.4 2.3.6 3.6.6.6 0 1 .4 1 1V20c0 .6-.4 1-1 1A17 17 0 0 1 3 4c0-.6.4-1 1-1h3.5c.6 0 1 .4 1 1 0 1.3.2 2.5.6 3.6.1.3 0 .7-.2 1z"/></svg>
      Call us : +1 888 888 8888
    </div>
  </header>

  <!-- hero -->
  <section class="abs hero" role="img" aria-label="Downtown city skyline with palm trees above a busy freeway">
    <div class="abs hero-disc"></div>
    <h1 class="abs hero-title">Tidemark<br>Consulting</h1>
    <div class="btn">Get Started <span class="dot"></span></div>
  </section>
  <svg class="abs hero-curve" width="1200" height="160" viewBox="0 0 1200 160">
    <path d="M0 70 Q600 200 1200 60 L1200 160 L0 160Z" fill="#74b81f"/>
    <path d="M0 88 Q600 226 1200 82 L1200 160 L0 160Z" fill="#fff"/>
  </svg>
  <div class="abs down">
    <svg width="40" height="40" viewBox="0 0 40 40"><path d="M20 12v16M14 22l6 6 6-6" stroke="#333" stroke-width="1.6" fill="none"/></svg>
  </div>

  <!-- about -->
  <h2 class="abs heading" style="left:112px;top:812px">ABOUT US<span class="rule"></span></h2>
  <div class="abs about-text">
    <p>Lorem ipsum dolor sit amet, consectetur adipiscing elit, sed do eiusmod tempor incididunt ut labore et dolore magna aliqua. Ut enim ad minim veniam, quis nostrud exercitation ullamco laboris nisi ut aliquip ex ea commodo consequat.</p>
    <p>Duis aute irure dolor in reprehenderit in voluptate velit esse cillum dolore eu fugiat nulla pariatur. Excepteur sint occaecat cupidatat non proident, sunt in culpa qui officia deserunt mollit anim id est laborum. Lorem ipsum dolor sit amet, consectetur adipiscing elit, sed do eiusmod tempor incididunt ut labore et dolore magna aliqua.</p>
  </div>
  <div class="btn" style="left:112px;top:1148px;width:153px;height:44px">Learn More <span class="dot"></span></div>
  <div class="abs about-mark">Tidemark</div>

  <!-- services -->
  <div class="abs services-bg"></div>
  <h2 class="abs heading" style="left:112px;top:1390px">OUR SERVICES<span class="rule"></span></h2>
  <svg class="abs chev" style="left:46px;top:1613px" viewBox="0 0 20 34"><path d="M17 2L3 17l14 15" stroke="#222" stroke-width="2" fill="none"/></svg>
  <svg class="abs chev" style="left:1133px;top:1613px" viewBox="0 0 20 34"><path d="M3 2l14 15L3 32" stroke="#222" stroke-width="2" fill="none"/></svg>
  <article class="abs card" style="left:112px">
    <div class="icon" role="img" aria-label="Shield in hand icon"></div>
    <h3>Safety &amp; Wellness</h3>
    <p>Lorem ipsum dolor sit amet, consec tetur adipiscing elit, sed do eiusmod tempor incididunt ut labore et dolore magna aliqua.</p>
    <div class="more">LEARN MORE ›</div>
  </article>
  <article class="abs card featured" style="left:445px">
    <div class="icon" role="img" aria-label="Globe and people icon"></div>
    <h3>Community Trust &amp; the Legitimacy of Policing</h3>
    <p>Lorem ipsum dolor sit amet, consec tetur adipiscing elit, sed do eiusmod tempor incididunt ut labore et dolore magna aliqua.</p>
    <div class="more">LEARN MORE ›</div>
  </article>
  <article class="abs card" style="left:777px">
    <div class="icon" role="img" aria-label="Person with raised hand icon"></div>
    <h3>Violence &amp; Force</h3>
    <p>Lorem ipsum dolor sit amet, consec tetur adipiscing elit, sed do eiusmod tempor incididunt ut labore et dolore magna aliqua.</p>
    <div class="more">LEARN MORE ›</div>
  </article>

  <!-- advisers -->
  <section class="abs advisers">
    <h2 class="abs heading" style="left:0;width:1200px;top:100px;text-align:center"><span class="rule"></span>PUBLIC SAFETY ADVISERS<span class="rule"></span></h2>
    <div class="abs tile green" style="left:112px;top:181px;width:243px;height:179px"><span class="glyph"></span>Nemo enim ipsam</div>
    <div class="abs tile white" style="left:355px;top:181px;width:243px;height:179px"><span class="glyph"></span>Nemo enim ipsam</div>
    <div class="abs photo" style="left:598px;top:181px;width:490px;height:225px" role="img" aria-label="Business team meeting around a laptop"></div>
    <div class="abs photo" style="left:112px;top:360px;width:486px;height:226px" role="img" aria-label="Two colleagues reviewing a document"></div>
    <div class="abs tile green" style="left:598px;top:406px;width:245px;height:180px"><span class="glyph"></span>Nemo enim ipsam</div>
    <div class="abs tile white" style="left:843px;top:406px;width:245px;height:180px"><span class="glyph"></span>Nemo enim ipsam</div>
    <div class="btn" style="left:523px;top:630px;width:154px;height:43px">View More <span class="dot"></span></div>
  </section>
  <svg class="abs" style="left:0;top:2567px" width="1200" height="84" viewBox="0 0 1200 84"><path d="M0 0 Q600 166 1200 0 V84 H0Z" fill="#fff"/></svg>

  <!-- blog -->
  <h2 class="abs heading" style="left:0;width:1200px;top:2752px;text-align:center"><span class="rule"></span>OUR BLOG<span class="rule"></span></h2>
  <svg class="abs chev" style="left:46px;top:3031px" viewBox="0 0 20 34"><path d="M17 2L3 17l14 15" stroke="#222" stroke-width="2" fill="none"/></svg>
  <svg class="abs chev" style="left:1133px;top:3031px" viewBox="0 0 20 34"><path d="M3 2l14 15L3 32" stroke="#222" stroke-width="2" fill="none"/></svg>
  <article class="abs post" style="left:110px">
    <div class="thumb" role="img" aria-label="Smiling businessman in an office"></div>
    <h4>Lorem ipsum dolor sit amet, consectetur</h4>
    <p>Lorem ipsum dolor sit amet, consec tet ur adipiscing elit, sed do eiusmod</p>
    <div class="meta"><span class="go"></span><span class="date">Jan 20,2023</span></div>
  </article>
  <article class="abs post" style="left:445px">
    <div class="thumb" role="img" aria-label="Colleagues working at a laptop"></div>
    <h4>Lorem ipsum dolor sit amet, consectetur</h4>
    <p>Lorem ipsum dolor sit amet, consec tet ur adipiscing elit, sed do eiusmod</p>
    <div class="meta"><span class="go"></span><span class="date">Jan 20,2023</span></div>
  </article>
  <article class="abs post" style="left:780px">
    <div class="thumb" role="img" aria-label="Business partners talking in a lounge"></div>
    <h4>Lorem ipsum dolor sit amet, consectetur</h4>
    <p>Lorem ipsum dolor sit amet, consec tet ur adipiscing elit, sed do eiusmod</p>
    <div class="meta"><span class="go"></span><span class="date">Jan 20,2023</span></div>
  </article>

  <!-- contact -->
  <section class="abs touch" role="img" aria-label="Faded office background in green tones">
    <h2 class="abs heading" style="left:0;width:1200px;top:88px;text-align:center"><span class="rule"></span>GET IN TOUCH<span class="rule"></span></h2>
  </section>
  <div class="abs field" style="left:263px;top:3513px;width:330px;height:44px">First Name</div>
  <div class="abs field" style="left:607px;top:3513px;width:329px;height:44px">Last Name</div>
  <div class="abs field" style="left:263px;top:3573px;width:330px;height:44px">Email address</div>
  <div class="abs field" style="left:607px;top:3573px;width:329px;height:44px">Phone</div>
  <div class="abs field" style="left:263px;top:3633px;width:673px;height:168px">Message</div>
  <div class="abs submit">SUBMIT NOW</div>

  <!-- footer -->
  <svg class="abs footer-curve" width="1200" height="80" viewBox="0 0 1200 80">
    <path d="M0 52 Q600 -10 1200 4 V80 H0Z" fill="#fff"/>
    <path d="M0 80 Q600 26 1200 30 V80 H0Z" fill="#0a3d85"/>
  </svg>
  <footer class="abs footer">
    <div class="frow" style="top:26px;gap:30px">
      <span><span class="ico"></span>123 Lorem ipsum dolor sit amet</span>
      <span><span class="ico" style="border-radius:1px;height:8px"></span>info@companyname.com</span>
      <span><span class="ico"></span>+1 888 888 8888</span>
    </div>
    <div class="frow" style="top:71px"><span>Home</span><span>|</span><span>About</span><span>|</span><span>Services</span><span>|</span><span>Blog</span><span>|</span><span>Contact</span></div>
    <div class="frow" style="top:114px"><span>Terms &amp; Conditions</span><span>|</span><span>Privacy Policy</span><span>|</span><span>Sitemap</span></div>
    <div class="frow" style="top:205px;font-size:12.5px"><span>©2023 Company name, All Rights Reserved</span></div>
  </footer>
  <div class="abs social" style="left:112px"></div>
  <div class="abs social" style="left:147px"></div>
  <div class="abs totop">
    <svg width="40" height="40" viewBox="0 0 40 40"><path d="M20 28V12M14 18l6-6 6 6" stroke="#333" stroke-width="1.6" fill="none"/></svg>
  </div>

</div>
</body>
</html>
```